Business Card for Graphic Design Firm

This project is for a new graphic design firm based in New Jersey called Velmoric. We outsource graphic design and marketing jobs. We want to communicate that this is a professional company but it as well creative and artistic. This card may be used as a horizontal double sided paper card or a vertical single sided translucent card so feel free to submit designs in whichever format or both.
Updates

Reason: Extending the deadline because I'm not exactly satisfied with the designs so far.

Please view the updated project brief

Target Market(s)

Adults aged 25-60

Industry/Entity Type

Graphic Design

Font styles to use
Serif
Sans Serif

Requirements
Nice to have
• Maybe a triangular pattern around the edges similar to our logo

```html
<!DOCTYPE html>
<html lang="en">
<head>
<meta charset="utf-8">
<title>Velmoric Business Card</title>
<link rel="stylesheet" href="https://fonts.googleapis.com/css2?family=Open+Sans:wght@300;400;600&display=swap">
<style>
  :root {
    --backdrop: #e7e4e0;
    --card-white: #ffffff;
    --brand-blue: #3e4a94;
    --accent-red: #dc4350;
    --accent-cyan: #27a8e6;
    --accent-yellow: #f6b33a;
    --accent-purple: #a445a0;
    --accent-navy: #3c3f8f;
    --text-gray: #6a6a6a;
    --line-gray: #9a9a9a;
  }
  * { margin: 0; padding: 0; box-sizing: border-box; }
  html, body { width: 1200px; height: 997px; overflow: hidden; }
  body {
    background: var(--backdrop);
    font-family: "Open Sans", Arial, sans-serif;
    position: relative;
  }
  .card {
    position: absolute;
    width: 520px;
    height: 297px;
    box-shadow: 0 10px 24px rgba(0,0,0,0.12);
  }
  /* Front side */
  .card-front {
    left: 60px; top: 230px;
    background: var(--brand-blue);
    color: #fff;
    text-align: center;
  }
  .front-name {
    position: absolute; left: 0; right: 0; top: 108px;
    font-size: 34px; font-weight: 600; letter-spacing: 2px;
  }
  .front-web {
    position: absolute; left: 0; right: 0; top: 176px;
    display: flex; align-items: center; justify-content: center; gap: 12px;
    font-size: 12px; letter-spacing: 3px;
  }
  .front-web::before, .front-web::after {
    content: ""; width: 52px; height: 1px; background: #fff;
  }
  /* Back side */
  .card-back {
    left: 620px; top: 470px;
    background: var(--card-white);
  }
  .back-brand {
    position: absolute; right: 34px; top: 58px;
    font-size: 28px; font-weight: 300; letter-spacing: 5px;
    color: var(--text-gray);
  }
  .brand-rule {
    position: absolute; right: 34px; top: 102px;
    width: 200px; height: 1px; background: var(--line-gray);
  }
  .address {
    position: absolute; right: 34px; top: 122px;
    font-size: 11px; line-height: 17px; color: var(--text-gray); text-align: right;
  }
  .person {
    position: absolute; left: 34px; top: 168px;
  }
  .person-name { font-size: 16px; font-weight: 600; color: var(--accent-red); }
  .person-role { font-size: 12px; color: var(--text-gray); margin-top: 1px; }
  .color-rule {
    position: absolute; left: 150px; right: 34px; top: 191px;
    height: 2px; display: flex;
  }
  .color-rule span { flex: 1; }
  .color-rule span + span { margin-left: 4px; }
  .contacts {
    position: absolute; left: 40px; top: 214px;
    list-style: none; font-size: 11px; color: var(--text-gray);
  }
  .contacts li { display: flex; align-items: center; gap: 8px; height: 16px; }
  .contacts svg { width: 11px; height: 11px; fill: var(--accent-red); }
</style>
</head>
<body>
  <section class="card card-front" aria-label="Card front">
    <div class="front-name">Velmoric</div>
    <div class="front-web">www.velmoric.com</div>
  </section>

  <section class="card card-back" aria-label="Card back">
    <div class="back-brand">VELMORIC</div>
    <div class="brand-rule"></div>
    <div class="address">Suite 210 Harbor Lane<br>Newark, NJ 07102, USA</div>

    <div class="person">
      <div class="person-name">Dana Whitlow</div>
      <div class="person-role">Director</div>
    </div>
    <div class="color-rule">
      <span style="background:var(--accent-cyan)"></span>
      <span style="background:var(--accent-yellow)"></span>
      <span style="background:var(--accent-red)"></span>
      <span style="background:var(--accent-purple)"></span>
      <span style="background:var(--accent-navy)"></span>
      <span style="background:var(--line-gray)"></span>
    </div>

    <ul class="contacts">
      <li><svg viewBox="0 0 12 12"><path d="M1 4c0-2 2-3 5-3s5 1 5 3l-2 1-1-1H4L3 5 1 4zM2 6h8l1 5H1z"/></svg>201 555 0147</li>
      <li><svg viewBox="0 0 12 12"><path d="M3 0h6a1 1 0 0 1 1 1v10a1 1 0 0 1-1 1H3a1 1 0 0 1-1-1V1a1 1 0 0 1 1-1zm0 2v7h6V2z"/></svg>201 555 0182</li>
      <li><svg viewBox="0 0 12 12"><path d="M3 0h6v4H3zM1 4h10v5H9v3H3V9H1zm3 4v3h4V8z"/></svg>201 555 0193</li>
      <li><svg viewBox="0 0 12 12"><path d="M0 2h12v8H0zm1 1v.5L6 7l5-3.5V3z"/></svg>hello@velmoric.com</li>
    </ul>
  </section>
</body>
</html>
```